Design NEW business card

We would like a business card using the colour deep red wine or dark navy blue textured background (patterned or not, open to suggestions) with a high gloss debossed rose gold/copper TM Thomas Marlow Jewellery business name (Provided). I have included images for your review we would like to keep our currently logo and business name on the front but you can change the layout and positioning. For the back of the card we are open to all suggestions/variations.
Use our current TM Thomas Marlow Jewellery logo (Provided image)

```html
<!DOCTYPE html>
<html lang="en">
<head>
<meta charset="utf-8">
<title>Thomas Marlow Jewellery – Business Cards</title>
<link href="https://fonts.googleapis.com/css2?family=Montserrat:wght@400;500;600&display=swap" rel="stylesheet">
<style>
  :root {
    --backdrop: #d6d6d6;
    --card-black: #1c1c1c;
    --card-white: #ffffff;
    --wine-light: #52191c;
    --wine-dark: #3a1012;
    --copper: #c98a5a;
    --copper-deep: #a8673f;
    --copper-debossed: #8e5640;
  }
  * { margin: 0; padding: 0; box-sizing: border-box; }
  html, body { width: 1200px; height: 815px; overflow: hidden; }
  body {
    background: var(--backdrop);
    font-family: "Montserrat", sans-serif;
    position: relative;
  }
  .card {
    position: absolute;
    width: 385px;
    height: 220px;
  }
  .card--front-dark { left: 175px; top: 117px; background: var(--card-black); color: var(--copper); }
  .card--front-light { left: 671px; top: 117px; background: var(--card-white); color: var(--copper-deep); }
  .card--back { background: radial-gradient(ellipse at 45% 40%, var(--wine-light), var(--wine-dark)); }
  .card--back-left { left: 171px; top: 449px; width: 389px; height: 228px; }
  .card--back-right { left: 672px; top: 449px; }

  .brand {
    position: absolute;
    left: 26px;
    top: 40px;
    display: flex;
    align-items: center;
    gap: 8px;
    font-size: 13px;
    font-weight: 500;
    letter-spacing: 0.04em;
  }
  .brand__dot { width: 8px; height: 8px; border-radius: 50%; background: currentColor; }

  .person { position: absolute; left: 26px; top: 135px; }
  .person__name { font-size: 17px; font-weight: 600; line-height: 1.1; }
  .person__role { font-size: 9.5px; font-weight: 500; margin-top: 2px; }

  .contact {
    position: absolute;
    left: 244px;
    top: 141px;
    font-size: 9.5px;
    font-weight: 500;
    line-height: 16px;
    list-style: none;
  }
  .contact__web { margin-top: 12px; }

  .back-mark {
    position: absolute;
    inset: 0;
    display: flex;
    flex-direction: column;
    align-items: center;
    justify-content: center;
    color: var(--copper-debossed);
    font-weight: 400;
    text-transform: uppercase;
  }
  .back-mark__name { font-size: 17px; letter-spacing: 0.32em; margin-top: 36px; }
  .back-mark__sub { font-size: 7px; letter-spacing: 0.9em; margin-top: 4px; }
</style>
</head>
<body>
  <section class="card card--front-dark">
    <div class="brand"><span class="brand__dot"></span>TM Thomas Marlow Jewellery</div>
    <div class="person">
      <p class="person__name">Daniel Reed</p>
      <p class="person__role">Co-Founder &amp; CEO</p>
    </div>
    <ul class="contact">
      <li>daniel@marlowstudio.com</li>
      <li>+44 20 7946 0321</li>
      <li class="contact__web">www.marlowstudio.com</li>
    </ul>
  </section>

  <section class="card card--front-light">
    <div class="brand"><span class="brand__dot"></span>TM Thomas Marlow Jewellery</div>
    <div class="person">
      <p class="person__name">Daniel Reed</p>
      <p class="person__role">Co-Founder &amp; CEO</p>
    </div>
    <ul class="contact">
      <li>daniel@marlowstudio.com</li>
      <li>+44 20 7946 0321</li>
      <li class="contact__web">www.marlowstudio.com</li>
    </ul>
  </section>

  <section class="card card--back card--back-left">
    <div class="back-mark">
      <p class="back-mark__name">Thomas Marlow</p>
      <p class="back-mark__sub">Jewellery</p>
    </div>
  </section>

  <section class="card card--back card--back-right">
    <div class="back-mark">
      <p class="back-mark__name">Thomas Marlow</p>
      <p class="back-mark__sub">Jewellery</p>
    </div>
  </section>
</body>
</html>
```